Eastgate AR Outfitters

Firearms Website

Requirements
Must have
• we are looking for two or three pages for a new company we are starting. The Name is Eastgate Arkansas Outfitters. The site will be EastgateArOutfitters.example (nothing on site at this time) We will be selling mainly handguns and products for self defense. We want this site to focus on the handgun and ammo sells as well as low cost transfers. we will handle the ecommerce part) We want a

1.) main page, mainly general information on the company.

2.) a page for sells. we will be adding the guns by hand as we place them for sell and use our credit card process. We just need the layout to fill in the items for sale on this page.

3.) navigation will be.. HOME - SALES (((guns and gun Accessories)) and self defense products) - Contact US- Transfers

company info

Eastgate Arkansas Outfitters

EastgateAROutfitters.example

sales@EastgateAROutfitters.example

855-Tool 2 Shop (855-555-0142) same number for fax

412 west Harlan avenue

Kosciusko, ms. 71234

```html
<!DOCTYPE html>
<html lang="en">
<head>
<meta charset="utf-8">
<title>Eastgate Arkansas Outfitters</title>
<link rel="stylesheet" href="https://fonts.googleapis.com/css2?family=PT+Sans:wght@400;700&family=Noto+Sans:wght@400;700&display=swap">
<style>
  :root {
    --bg-top: #0c0c0c;
    --bg-main: #111111;
    --accent: #00aeef;
    --tab-active: #c9c9c9;
    --text-white: #ffffff;
    --text-body: #8c8c8c;
    --text-list: #9a9a9a;
    --rule: #2c2c2c;
    --button: #3a3a3a;
  }
  * { margin: 0; padding: 0; box-sizing: border-box; }
  html, body { width: 1200px; height: 1200px; overflow: hidden; }
  body {
    position: relative;
    background: var(--bg-main);
    font-family: "Noto Sans", Verdana, sans-serif;
    color: var(--text-white);
  }
  .page-glow {
    position: absolute; left: 0; top: 175px; width: 1200px; height: 1025px;
    background: radial-gradient(ellipse 620px 520px at 600px 420px, #2a2a2a 0%, #161616 55%, #050505 100%);
  }
  .header-band {
    position: absolute; left: 0; top: 0; width: 1200px; height: 175px;
    background: var(--bg-top);
  }
  .brand {
    position: absolute; left: 112px; top: 34px; width: 240px;
    font-family: "PT Sans", Tahoma, sans-serif; font-size: 25px; line-height: 30px;
    color: var(--text-white);
  }
  .brand span { display: block; }
  .brand span:last-child { padding-left: 60px; }
  .social {
    position: absolute; left: 853px; top: 32px; display: flex; align-items: center; gap: 6px;
    font-family: "PT Sans", Tahoma, sans-serif; font-size: 15px;
  }
  .social-label { margin-right: 4px; }
  .social-square { width: 30px; height: 30px; background: var(--accent); }
  .contact-line {
    position: absolute; left: 865px; top: 90px;
    font-family: "PT Sans", Tahoma, sans-serif; font-size: 15px;
  }
  .contact-line .number { font-size: 13px; color: #d8d8d8; }
  .nav {
    position: absolute; left: 151px; top: 148px; width: 900px; height: 54px;
    background: var(--accent); border-radius: 0 4px 0 0;
  }
  .nav-item {
    position: absolute; top: 0; height: 54px; line-height: 54px;
    font-family: "PT Sans", Tahoma, sans-serif; font-size: 16px; font-weight: 700; color: var(--text-white);
    text-align: center;
  }
  .nav-item.is-active { left: 0; width: 131px; background: var(--tab-active); color: #111; }
  .search {
    position: absolute; left: 644px; top: 14px; width: 243px; height: 26px;
    background: #fff; border-radius: 3px; font-size: 11px; color: #222; padding: 5px 8px;
  }
  .search svg { position: absolute; right: 7px; top: 5px; }
  .search .divider { position: absolute; right: 33px; top: 5px; width: 1px; height: 16px; border-left: 1px dotted #999; }
  .hero {
    position: absolute; left: 100px; top: 223px; width: 1000px; height: 400px;
    background: linear-gradient(90deg, #f4f4f4 0%, #d9d9d9 30%, #ffffff 55%, #e6cf8f 75%, #c9a44c 100%);
  }
  .slider-arrow { position: absolute; top: 385px; }
  .section-title {
    position: absolute; font-family: "PT Sans", Tahoma, sans-serif; font-size: 27px; font-weight: 400;
    color: var(--text-white);
  }
  .body-copy {
    position: absolute; left: 112px; top: 707px; width: 675px;
    font-size: 11px; line-height: 15.8px; color: var(--text-body);
  }
  .body-copy p + p { margin-top: 16px; }
  .product { position: absolute; top: 933px; width: 249px; }
  .product-photo { width: 249px; height: 154px; border: 2px solid #2a2a2a; }
  .product-photo.light { background: radial-gradient(circle at 50% 45%, #d7a66a 0%, #f0e6dc 35%, #ffffff 70%); border-color: #e0e0e0; }
  .product-photo.brass { background: radial-gradient(circle, #d9b55a 0%, #a9822f 55%, #4a3714 100%); }
  .product-caption { margin-top: 12px; font-size: 11px; font-weight: 700; text-align: center; padding-right: 40px; }
  .column-rule { position: absolute; left: 821px; top: 695px; width: 1px; height: 340px; background: var(--rule); }
  .weapon-list { position: absolute; left: 852px; top: 712px; width: 219px; list-style: none; border-top: 1px solid var(--rule); }
  .weapon-list li {
    height: 50px; line-height: 50px; padding-left: 8px;
    border-bottom: 1px solid var(--rule); font-size: 11px; color: var(--text-list);
  }
  .read-more {
    position: absolute; left: 992px; top: 1083px; width: 80px; height: 25px; line-height: 25px;
    background: var(--button); color: #aaa; font-size: 12px; text-align: center;
  }
  .footer-rule { position: absolute; left: 100px; top: 1145px; width: 1000px; height: 1px; background: var(--rule); }
  .copyright { position: absolute; left: 102px; top: 1169px; font-size: 11px; font-weight: 700; }
</style>
</head>
<body>
  <div class="page-glow"></div>
  <header class="header-band">
    <div class="brand"><span>Eastgate Arkansas</span><span>Outfitters</span></div>
    <div class="social">
      <span class="social-label">Social Media :</span>
      <span class="social-square"></span>
      <span class="social-square"></span>
      <span class="social-square"></span>
    </div>
    <div class="contact-line">Contact No : <span class="number">000 000 0000</span></div>
  </header>

  <nav class="nav">
    <div class="nav-item is-active">Home</div>
    <div class="nav-item" style="left:170px;width:125px;">About us</div>
    <div class="nav-item" style="left:325px;width:120px;">Services</div>
    <div class="nav-item" style="left:470px;width:115px;">Contact us</div>
    <div class="search">Search
      <span class="divider"></span>
      <svg width="16" height="16" viewBox="0 0 16 16"><circle cx="6" cy="6" r="4.5" fill="none" stroke="#333" stroke-width="1.5"/><line x1="9.5" y1="9.5" x2="14" y2="14" stroke="#333" stroke-width="2"/></svg>
    </div>
  </nav>

  <div class="hero" role="img" aria-label="Banner photo of a silver revolver and a row of rifle and pistol cartridges with the heading Gun And Ammo"></div>
  <svg class="slider-arrow" style="left:42px" width="26" height="44" viewBox="0 0 26 44"><polyline points="23,2 3,22 23,42" fill="none" stroke="#fff" stroke-width="2.5"/></svg>
  <svg class="slider-arrow" style="left:1142px" width="26" height="44" viewBox="0 0 26 44"><polyline points="3,2 23,22 3,42" fill="none" stroke="#fff" stroke-width="2.5"/></svg>

  <h1 class="section-title" style="left:112px;top:655px;">Welcome to Our Website</h1>
  <div class="body-copy">
    <p>Lorem ipsum dolor sit amet, consectetur adipiscing elit is all my as. Cramsuada Lorem ipsum dolor sit amet, consectetur adipiscing elit is all my as. Cramsuada lobortis semper. Duis non posuere orci. Vestibulum at sagittis,felis in accumsans is a faubus, orci leo cursus felis, nec mattis turpis sapien sed ante.lobortis semper.</p>
    <p>Duis non posuere orci. Vestibulum at sagittis,felis in accumsans is a<br>faubus, orci leo cursus felis, nec mattis turpis sapien sed ante.Lorem ipsum dolor sit amet, consectetur adipiscing elit is all my as. Cramsuada Lorem ipsum dolor sit amet, consectetur adipiscing Lorem ipsum dolor sit amet, consectetur adipiscing elit is all my as. elit is all my as. Cramsuada lobortis semper. Duis non posuere orci. Vestibulum at sagittis,felis in accumsans is a faubus, orci leo cursus felis, nec mattis turpis sapien sed ante.lobortis semper. Duis non posuere orci. Vestibulum at sagittis,felis in accumsans is a faubus, orci leo cursus felis, nec mattis turpis sapien sed ante.</p>
  </div>

  <h2 class="section-title" style="left:112px;top:885px;">Ammo Sells</h2>
  <div class="product" style="left:112px;">
    <div class="product-photo light" role="img" aria-label="Photo of two copper pistol cartridges"></div>
    <div class="product-caption">Lorem Ipsum</div>
  </div>
  <div class="product" style="left:441px;">
    <div class="product-photo brass" role="img" aria-label="Photo of a pile of brass pistol cartridges"></div>
    <div class="product-caption">Lorem Ipsum</div>
  </div>

  <div class="column-rule"></div>
  <h2 class="section-title" style="left:843px;top:655px;">Popular Weapons</h2>
  <ul class="weapon-list">
    <li>Lorem ipsum dolor sit amet</li>
    <li>Lorem ipsum dolor sit amet</li>
    <li>Lorem ipsum dolor sit amet</li>
    <li>Lorem ipsum dolor sit amet</li>
    <li>Lorem ipsum dolor sit amet</li>
    <li>Lorem ipsum dolor sit amet</li>
    <li>Lorem ipsum dolor sit amet</li>
  </ul>
  <div class="read-more">Read More</div>

  <div class="footer-rule"></div>
  <footer class="copyright">© Copyright 2013</footer>
</body>
</html>
```